Tech business card design

We need an amazing business card design for our new business 'Brakka' a marketing tech startup based in Sydney, Australia. We provide an online marketplace for businesses to search and buy advertising media, connect with service providers and learn more about marketing. We wish to communicate 'cool tech', reliability and professionalism and design based around our logo.

Target Market(s)

Business Owners

Contact Information for Business Card

Name
Position
Email Address
Website
Phone Number

Font styles to use
Other font styles liked:
• Avenir & Avenir Next

Colors

Designer to choose colors to be used in the design.

```html
<!DOCTYPE html>
<html lang="en">
<head>
<meta charset="utf-8">
<title>Brakka Business Card</title>
<link href="https://fonts.googleapis.com/css2?family=Nunito+Sans:wght@400;600;800&display=swap" rel="stylesheet">
<style>
  :root {
    --backdrop: #e8ebed;
    --navy-light: #30358f;
    --navy-dark: #16163f;
    --navy-ink: #1d1f52;
    --navy-ghost: rgba(255, 255, 255, 0.06);
    --paper: #ffffff;
    --paper-ghost: #eef0f2;
    --ink: #2b2d3a;
    --muted: #5c5f6e;
    --url-light: #c9cbe6;
  }
  * { box-sizing: border-box; margin: 0; padding: 0; }
  html, body {
    width: 1200px; height: 900px; overflow: hidden;
    background: var(--backdrop);
    font-family: "Nunito Sans", "Avenir Next", Avenir, sans-serif;
  }
  .stage {
    width: 1200px; height: 900px;
    display: flex; flex-direction: column; align-items: center; justify-content: center;
    gap: 50px;
  }
  .card {
    position: relative; width: 560px; height: 320px; overflow: hidden;
    border-radius: 4px;
    box-shadow: 0 14px 30px rgba(20, 24, 50, 0.18);
  }
  .wordmark { font-weight: 800; letter-spacing: -1px; line-height: 1; }
  .wordmark .tm { font-size: 12px; font-weight: 600; letter-spacing: 0; vertical-align: top; margin-left: 3px; }
  .ghost-word {
    position: absolute; font-weight: 800; letter-spacing: -6px; line-height: 1;
    font-size: 230px; white-space: nowrap;
  }

  /* Front */
  .card-front {
    background: linear-gradient(160deg, var(--navy-light) 0%, #22246a 50%, var(--navy-dark) 100%);
  }
  .card-front .ghost-word { color: var(--navy-ghost); left: -60px; top: 20px; }
  .front-brand {
    position: absolute; left: 0; right: 0; top: 112px; text-align: center; color: var(--paper);
  }
  .front-brand .wordmark { font-size: 72px; }
  .front-brand .url { margin-top: 10px; font-size: 15px; letter-spacing: 0.5px; color: var(--url-light); }

  /* Back */
  .card-back { background: var(--paper); }
  .card-back .ghost-word { color: var(--paper-ghost); left: -30px; top: 10px; }
  .back-brand { position: absolute; left: 46px; bottom: 50px; color: var(--navy-ink); }
  .back-brand .wordmark { font-size: 64px; }
  .contact { position: absolute; left: 322px; top: 64px; color: var(--ink); }
  .contact .name { font-size: 18px; font-weight: 800; color: var(--navy-ink); letter-spacing: 0.3px; }
  .contact .role { font-size: 12px; color: var(--muted); margin-top: 2px; margin-bottom: 18px; }
  .contact ul { list-style: none; }
  .contact li { display: flex; align-items: center; gap: 10px; font-size: 13px; margin-bottom: 9px; }
  .contact svg { width: 14px; height: 14px; flex: none; fill: var(--navy-ink); }
</style>
</head>
<body>
<main class="stage">
  <section class="card card-front">
    <div class="ghost-word" aria-hidden="true">brakka</div>
    <div class="front-brand">
      <div class="wordmark">brakka<span class="tm">™</span></div>
      <div class="url">www.brakkamedia.com.au</div>
    </div>
  </section>

  <section class="card card-back">
    <div class="ghost-word" aria-hidden="true">brakka</div>
    <div class="back-brand">
      <div class="wordmark">brakka<span class="tm">™</span></div>
    </div>
    <div class="contact">
      <div class="name">DANIEL REYES</div>
      <div class="role">Founder | Director</div>
      <ul>
        <li>
          <svg viewBox="0 0 14 14" aria-hidden="true"><path d="M3.5 0h7a1 1 0 0 1 1 1v12a1 1 0 0 1-1 1h-7a1 1 0 0 1-1-1V1a1 1 0 0 1 1-1zm.5 1.5v9.5h6V1.5zM7 11.6a.8.8 0 1 0 0 1.6.8.8 0 0 0 0-1.6z"/></svg>
          +61 (0)400 555 218
        </li>
        <li>
          <svg viewBox="0 0 14 14" aria-hidden="true"><path d="M0 3h14v9H0zm1.5 1.2v.3L7 8.2l5.5-3.7v-.3zm0 2v4.3h11V6.2L7 9.9z"/></svg>
          daniel@brakkamedia.com.au
        </li>
        <li>
          <svg viewBox="0 0 14 14" aria-hidden="true"><path d="M7 0a7 7 0 1 0 0 14A7 7 0 0 0 7 0zm4.9 6.2H9.8a10 10 0 0 0-.9-4 5.6 5.6 0 0 1 3 4zM7 1.5c.6.7 1.2 2.3 1.3 4.7H5.7C5.8 3.8 6.4 2.2 7 1.5zM5.1 2.2a10 10 0 0 0-.9 4H2.1a5.6 5.6 0 0 1 3-4zM2.1 7.8h2.1a10 10 0 0 0 .9 4 5.6 5.6 0 0 1-3-4zM7 12.5c-.6-.7-1.2-2.3-1.3-4.7h2.6c-.1 2.4-.7 4-1.3 4.7zm1.9-.7a10 10 0 0 0 .9-4h2.1a5.6 5.6 0 0 1-3 4z"/></svg>
          www.brakkamedia.com.au
        </li>
      </ul>
    </div>
  </section>
</main>
</body>
</html>
```